Lumen Heat Flow Studio – Corporate Brand Identity

We are in need of a full company image and brand identity design for a brand new hot yoga studio in a small but busy and wealthy oil town.
Our logo was designed through artbazaar and we currently have an open wordpress project in artbazaar with a deadline of July 14. We plan on continuing to build our marketing presence through artbazaar or one on one with designers that have been able to capture our vision easily. So, there are many more opportunities for continued projects.
We love our current logo and would like it to be utilized well. We want our logo to be familiar, known and synonymous with hot yoga in Alberta, Canada. We have intentions of opening up more locations and are looking for a strong brand that we can eventually franchise.
We need to display a strong but serene image that demands awe and communicates to people that Lumen Heat Flow is the real deal and will provide them with exactly what they need. Our studio is the perfect balance of what you would gain from going to a gym and developing your physical fitness and visiting a spa and nurturing a quiet mind, calm spirit and finding relaxation. We are all of this in one place. Breathe. Bend. Beam. – Steady Frame. Still Heart. Clear Soul.
In every detail our brand image should feel that “we are it.. the real deal when it comes to yoga…the place you want to be… the community you want to be apart of”. We need to appeal to men and women and a very important part of our business will be offering corporate packages and workplace yoga to the large oil companies in town. Our clientele is affluent so although we want creativity it still needs to be posh and upscale.
Most importantly, we are looking for something that is extraordinarily creative and show stopping. We want to set ourselves apart from all other studios in Canada, in terms of our creative, beautiful print marketing. When I say innovative, I’m thinking outside the box as in we want to be known for having beautiful and creative brand image http://www.quirkyfennel.com/fitness-and-yoga-ads/ I also like the idea of utilizing an image of the most beautiful oasis – see http://markgallerio.com/tulsi-flow-studio/
We are in need of at least the following:
- Business Cards – Front & Back
- Standard Letterhead (Size A4)
- Continuation Letterhead
- Envelopes (Sizes C4 & A4, , C5, DL)
- Postcard (for voucher, birthday, marketing)
- Loyalty Card design (front and back) for 10 visits
- Gift Certificate design
- Presentation Folder (for corporate packages)
- Standard Invoice A4 (word template)
- With Compliments Slips A5 (word template)
- Email Signature
OPTIONAL
- Labels for Branded Retail Products (Mat Spray, Room Spray, Aromatherapy)
- Social Media (Facebook Cover, etc)
All items must be editable in regards to changing names, addresses, etc. and high resolution please.
Please let me know if you require the logo in another format - ie. "ai, eps"

```html
<!DOCTYPE html>
<html lang="en">
<head>
<meta charset="utf-8">
<title>Lumen Heat Flow Studio – Business Card</title>
<link rel="stylesheet" href="https://fonts.googleapis.com/css2?family=Josefin+Sans:wght@400;600&display=swap">
<style>
  :root {
    --backdrop: #eeeff0;
    --card-white: #f6f7f7;
    --card-grey: #e4e6e7;
    --teal: #6cbfcd;
    --teal-light: #8fd0da;
    --deep-green: #1f7d6c;
    --brand: #2f8f86;
    --ink: #1f4f55;
    --sky: #dfe5ea;
    --sand: #e6d8bd;
    --palm: #9aa886;
  }
  * { box-sizing: border-box; margin: 0; padding: 0; }
  html, body { width: 1200px; height: 795px; overflow: hidden; }
  body {
    background: var(--backdrop);
    font-family: "Josefin Sans", sans-serif;
    position: relative;
  }
  .business-card {
    position: absolute;
    top: 243px;
    width: 540px;
    height: 309px;
    overflow: hidden;
    box-shadow: 0 6px 18px rgba(0,0,0,0.12);
  }
  .card-front { left: 40px; }
  .card-back { left: 620px; background: linear-gradient(135deg, var(--card-white), var(--card-grey)); }

  .desert-photo {
    position: absolute; inset: 0;
    background: linear-gradient(180deg, var(--sky) 0%, var(--sand) 32%, var(--palm) 52%, var(--sand) 70%, #d9d3bf 100%);
    opacity: 0.85;
  }
  .card-wave { position: absolute; inset: 0; width: 100%; height: 100%; }

  .brand-mark {
    position: absolute;
    display: flex; align-items: center; gap: 10px;
    color: var(--brand);
    font-weight: 600;
    letter-spacing: 0.06em;
    text-transform: uppercase;
    white-space: nowrap;
  }
  .brand-mark .brand-dot {
    border-radius: 50%;
    background: var(--brand);
    flex: none;
  }
  .card-front .brand-mark { left: 90px; top: 116px; font-size: 24px; }
  .card-front .brand-dot { width: 32px; height: 32px; }
  .card-back .brand-mark { left: 50px; top: 56px; font-size: 13px; gap: 7px; }
  .card-back .brand-dot { width: 18px; height: 18px; }

  .holder {
    position: absolute; left: 26px; top: 118px;
    color: var(--ink);
    font-size: 11px; letter-spacing: 0.2em; text-transform: uppercase;
  }
  .holder .holder-name { font-weight: 600; }
  .holder .holder-role { margin-top: 3px; font-size: 9px; }

  .contact-list {
    position: absolute; left: 200px; top: 160px;
    list-style: none;
    color: var(--ink);
    font-size: 10px; letter-spacing: 0.1em; line-height: 14px;
    white-space: nowrap;
  }
  .contact-list li { display: flex; align-items: center; gap: 8px; }
  .contact-list li:first-child { margin-bottom: 5px; }
  .contact-list svg { width: 9px; height: 9px; flex: none; fill: var(--ink); }
</style>
</head>
<body>

  <section class="business-card card-front" aria-label="Business card front">
    <div class="desert-photo" role="img" aria-label="Desert landscape photograph: sand dunes, palm trees and still water reflecting them"></div>
    <svg class="card-wave" viewBox="0 0 540 309" preserveAspectRatio="none" aria-hidden="true">
      <path d="M0 270 C140 255 300 230 430 190 C480 176 515 170 540 168 L540 309 L0 309 Z" fill="var(--deep-green)"/>
      <path d="M0 278 C150 262 300 240 430 202 C480 188 515 182 540 181 L540 309 L0 309 Z" fill="var(--teal)"/>
    </svg>
    <div class="brand-mark"><span class="brand-dot"></span>Lumen Heat Flow Studio</div>
  </section>

  <section class="business-card card-back" aria-label="Business card back">
    <svg class="card-wave" viewBox="0 0 540 309" preserveAspectRatio="none" aria-hidden="true">
      <path d="M0 102 C120 96 240 110 340 130 C430 148 490 150 540 155 L540 309 L0 309 Z" fill="var(--teal-light)"/>
      <path d="M0 108 C120 104 240 120 340 142 C430 162 490 168 540 176 L540 309 L0 309 Z" fill="var(--teal)"/>
      <path d="M490 164 C510 167 528 169 540 170 L540 205 C525 195 510 182 490 164 Z" fill="var(--deep-green)"/>
    </svg>
    <div class="brand-mark"><span class="brand-dot"></span>Lumen Heat Flow Studio</div>

    <div class="holder">
      <div class="holder-name">Daniel Ruhl</div>
      <div class="holder-role">CEO</div>
    </div>

    <ul class="contact-list">
      <li><svg viewBox="0 0 10 10"><path d="M5 0a3.5 3.5 0 0 0-3.5 3.5C1.5 6 5 10 5 10s3.5-4 3.5-6.5A3.5 3.5 0 0 0 5 0zm0 5a1.5 1.5 0 1 1 0-3 1.5 1.5 0 0 1 0 3z"/></svg>Lindenweg 8, T9K 2P4 Fort Aster, Canada</li>
      <li><svg viewBox="0 0 10 10"><path d="M2 0h2l1 2.5-1.3 1a6 6 0 0 0 2.8 2.8l1-1.3L10 6v2a2 2 0 0 1-2 2A8 8 0 0 1 0 2a2 2 0 0 1 2-2z"/></svg>+1 780 210 4837</li>
      <li><svg viewBox="0 0 10 10"><rect x="2.5" y="0" width="5" height="10" rx="1"/></svg>+1 780 340 6219</li>
      <li><svg viewBox="0 0 10 10"><path d="M0 2h10v6H0z M0 2l5 3.5L10 2" /></svg>daniel.ruhl@lumenheatflow.ca</li>
      <li><svg viewBox="0 0 10 10"><circle cx="5" cy="5" r="4.5"/></svg>www.lumenheatflow.ca</li>
    </ul>
  </section>

</body>
</html>
```